Business Card Design

Need business card design for all carpentry & construction solutions. We would like to see designs that use black as a background with orange writing as it would stand out.

Business

KRV CONTRACTING
MARTIN COLBY
14 PELLINGTON ST
MARRINUP VALE
WA 6581
0498371265
krvcontracting@tramlex.com

```html
<!DOCTYPE html>
<html lang="en">
<head>
<meta charset="utf-8">
<title>Martin Colby – Business Card</title>
<link rel="stylesheet" href="https://fonts.googleapis.com/css2?family=Arimo:wght@400;700&family=Questrial&display=swap">
<style>
  :root {
    --card-bg: #000000;
    --ink-orange: #f27a36;
  }
  html, body {
    margin: 0;
    padding: 0;
    width: 1200px;
    height: 741px;
    overflow: hidden;
    background: var(--card-bg);
  }
  .business-card {
    display: block;
    width: 1200px;
    height: 741px;
    background: var(--card-bg);
  }
  .contact-block text {
    fill: var(--ink-orange);
    text-anchor: middle;
  }
  .contact-name {
    font-family: "Arimo", Arial, sans-serif;
    font-weight: 700;
    font-size: 45px;
  }
  .contact-line {
    font-family: "Questrial", "Century Gothic", sans-serif;
    font-size: 39px;
  }
  .contact-email {
    font-family: "Arimo", Arial, sans-serif;
    font-weight: 400;
    font-size: 42px;
  }
</style>
</head>
<body>
  <svg class="business-card" width="1200" height="741" viewBox="0 0 1200 741" xmlns="http://www.w3.org/2000/svg">
    <rect width="1200" height="741" fill="var(--card-bg)"/>
    <g class="contact-block">
      <text class="contact-name" x="600" y="249">Martin Colby</text>
      <text class="contact-line" x="600" y="304">14 Pellington St</text>
      <text class="contact-line" x="600" y="359">Marrinup Vale</text>
      <text class="contact-line" x="600" y="411">WA 6581</text>
      <text class="contact-line" x="600" y="465">049-837-1265</text>
      <text class="contact-email" x="600" y="579">krvcontracting@tramlex.com</text>
    </g>
  </svg>
</body>
</html>
```